K & R Ground Works. Business card design

We need a business card designed for a new business. We have a bulldozer and tractor service. We clear land and make wildlife food plots. We provide disking, bush hogging, and site prep services.
I have attached an image of a business card that I like and would like my business cards to look similar.

Target Market(s)

anyone needing bulldozer and/or tractor services

Industry/Entity Type

Business

Contact Information for Business Card

K & R Ground Works, Operated by 7-T-Ranch
Dale Whitcomb
601-555-0148
dwk4821@mailbarn.example

Font styles to use
Sans Serif

Colors

Designer to choose colors to be used in the design.

Requirements
Must have
• image of tractor and bulldozer
• Land Clearing
• Wildlife food plots
• Bush Hogging
• Disking
• Site prep
Nice to have
• i have included a image of a business card that i like. I would like mine to be similar.

```html
<!DOCTYPE html>
<html lang="en">
<head>
<meta charset="utf-8">
<title>K &amp; R Ground Works – Business Card</title>
<link href="https://fonts.googleapis.com/css2?family=Arimo:wght@400;700&family=Open+Sans:wght@700&family=Source+Sans+3:wght@400&display=swap" rel="stylesheet">
<style>
  :root {
    --backdrop: #e9e6e1;
    --card: #ffffff;
    --accent-orange: #e06a12;
    --text-grey: #4a4a4a;
    --brand-brown: #5a3a1e;
    --rule-grey: #8a8a8a;
    --service-brown: #4b2e1a;
  }
  html, body {
    margin: 0;
    width: 1200px;
    height: 900px;
    overflow: hidden;
    background: var(--backdrop);
  }
  .business-card {
    position: absolute;
    left: 406px;
    top: 134px;
    width: 445px;
    height: 718px;
    background: var(--card);
    box-shadow: 2px 3px 8px rgba(0,0,0,0.35);
    overflow: hidden;
  }
  .contact {
    position: absolute;
    top: 49px;
    width: 100%;
    text-align: center;
    font-family: "Arimo", Arial, sans-serif;
  }
  .contact-name {
    margin: 0;
    font-size: 29px;
    font-weight: 700;
    color: var(--accent-orange);
    line-height: 1;
  }
  .contact-line {
    margin: 0;
    font-size: 22px;
    color: var(--text-grey);
    line-height: 30px;
  }
  .contact-name + .contact-line { margin-top: 13px; }
  .brand-mark {
    position: absolute;
    top: 196px;
    left: 50%;
    width: 64px;
    height: 64px;
    margin-left: -32px;
    display: block;
  }
  .brand {
    position: absolute;
    top: 288px;
    width: 100%;
    text-align: center;
  }
  .brand-name {
    margin: 0;
    font-family: "Open Sans", Arial, sans-serif;
    font-weight: 700;
    font-size: 25px;
    letter-spacing: -0.5px;
    color: var(--brand-brown);
    text-transform: uppercase;
    line-height: 1.2;
  }
  .brand-tagline {
    display: flex;
    align-items: center;
    justify-content: center;
    gap: 10px;
    margin: 2px 0 0;
    font-family: "Open Sans", Arial, sans-serif;
    font-weight: 700;
    font-size: 15px;
    color: var(--text-grey);
    text-transform: uppercase;
  }
  .brand-tagline::before,
  .brand-tagline::after {
    content: "";
    width: 48px;
    height: 1px;
    background: var(--rule-grey);
  }
  .equipment-photos {
    position: absolute;
    top: 361px;
    left: 0;
    width: 100%;
    height: 245px;
    display: flex;
  }
  .photo-bulldozer {
    width: 266px;
    height: 100%;
    background: linear-gradient(180deg, #6f9a4a 0%, #4f7a35 35%, #b79a3a 55%, #8a7a55 78%, #7a6a4a 100%);
  }
  .photo-tractor {
    flex: 1;
    height: 100%;
    background: linear-gradient(180deg, #5a8fd0 0%, #7ea7d8 18%, #3f6e2c 40%, #d9562a 60%, #7d8a50 80%, #8a9660 100%);
  }
  .services {
    position: absolute;
    top: 628px;
    width: 100%;
    text-align: center;
    font-family: "Source Sans 3", "Myriad Pro", sans-serif;
    font-size: 24px;
    color: var(--service-brown);
    line-height: 30px;
  }
  .services p { margin: 0; }
</style>
</head>
<body>
  <article class="business-card">
    <header class="contact">
      <h1 class="contact-name">Dale Whitcomb</h1>
      <p class="contact-line">Tel: 601-555-0148</p>
      <p class="contact-line">Email: dwk4821@mailbarn.example</p>
    </header>

    <svg class="brand-mark" viewBox="0 0 64 64" aria-hidden="true">
      <circle cx="32" cy="32" r="30" fill="var(--accent-orange)"/>
    </svg>

    <section class="brand">
      <p class="brand-name">K &amp; R Ground Works</p>
      <p class="brand-tagline">Operated by 7-T-Ranch</p>
    </section>

    <section class="equipment-photos">
      <div class="photo-bulldozer" role="img" aria-label="Photo of a yellow bulldozer clearing land in front of green trees"></div>
      <div class="photo-tractor" role="img" aria-label="Photo of an orange tractor with front loader on a grassy field"></div>
    </section>

    <footer class="services">
      <p>Land Clearing | Wildlife Food Plots</p>
      <p>Bush Hogging | Disking | Site Prep</p>
    </footer>
  </article>
</body>
</html>
```